Lucia Verena a furniture, interior design and home decor Brand

I need complete stationary for a new brand, business card, postcard, letter head, shipping envelopes, tissue paper, etc... I would like to use copper foil on some of these items. I have a logo design. I would like to see

Target Market(s)

Furniture,Interior Design & Home Decor

Industry/Entity Type

Interior Design

Colors
606060
7f7f7f

Requirements
Must have
• My signature style is spanish medeterrenean, my brand colors is charcoal gray with copper. Would love to see a wrought iron panel illustration created, I have attahced a few samples of wrought iron illustration I am attracted to, also an example of packing that has the pattern in foil.
Should not have
• Will not be using the word Design, only Lucia Verena and LV icon

```html
<!DOCTYPE html>
<html lang="en">
<head>
<meta charset="utf-8">
<title>Lucia Verena — Envelopes</title>
<link href="https://fonts.googleapis.com/css2?family=Cormorant+Garamond:wght@500&family=Montserrat:wght@400&display=swap" rel="stylesheet">
<style>
  :root {
    --backdrop: #e4e2df;
    --paper: #f3f3f2;
    --paper-edge: #dcdcda;
    --copper: #c0683a;
    --copper-light: #e0a27a;
    --flap: #b9572a;
    --ink: #4a4a4a;
  }
  * { margin: 0; padding: 0; box-sizing: border-box; }
  html, body { width: 1200px; height: 794px; overflow: hidden; background: var(--backdrop); }
  .sheet { position: relative; width: 1200px; height: 794px; }
  .envelope {
    position: absolute; top: 262px; width: 540px; height: 270px;
    background: var(--paper); border: 1px solid var(--paper-edge);
    box-shadow: 0 6px 18px rgba(0,0,0,.12); overflow: hidden;
  }
  .envelope--front { left: 40px; }
  .envelope--back { left: 620px; }
  .front-arc { position: absolute; left: 50px; top: -70px; }
  .brand-lockup {
    position: absolute; left: 300px; top: 112px;
    display: flex; align-items: center; gap: 12px;
  }
  .brand-mark { width: 40px; height: 40px; border: 1.5px solid var(--copper); border-radius: 50%; }
  .brand-divider { width: 1px; height: 36px; background: var(--copper); }
  .brand-name {
    font-family: "Cormorant Garamond", serif; font-weight: 500;
    font-size: 26px; color: var(--copper); letter-spacing: .5px;
  }
  .return-address {
    position: absolute; right: 24px; bottom: 20px;
    font-family: "Montserrat", sans-serif; font-size: 9px; color: var(--ink); letter-spacing: .4px;
  }
  .flap {
    position: absolute; left: 0; top: 0; width: 100%; height: 78px;
    background: var(--flap); display: flex; align-items: center; justify-content: center; gap: 10px;
  }
  .flap-mark { width: 26px; height: 26px; border: 1.2px solid #fff; border-radius: 50%; }
  .flap-initials {
    font-family: "Cormorant Garamond", serif; font-weight: 500;
    font-size: 22px; color: #fff; letter-spacing: 1px;
  }
</style>
</head>
<body>
<main class="sheet">
  <section class="envelope envelope--front" aria-label="Envelope front">
    <svg class="front-arc" width="250" height="250" viewBox="0 0 250 250" aria-hidden="true">
      <defs>
        <linearGradient id="copperGradient" x1="0" y1="0" x2="1" y2="1">
          <stop offset="0" stop-color="var(--copper-light)"/>
          <stop offset="1" stop-color="var(--copper)"/>
        </linearGradient>
      </defs>
      <circle cx="125" cy="125" r="118" fill="none" stroke="url(#copperGradient)" stroke-width="2.5"/>
    </svg>
    <div class="brand-lockup">
      <span class="brand-mark"></span>
      <span class="brand-divider"></span>
      <span class="brand-name">Lucia Verena</span>
    </div>
    <p class="return-address">48 Harbor Lane, Westbrook, ON, K2B 4C7</p>
  </section>

  <section class="envelope envelope--back" aria-label="Envelope back">
    <div class="flap">
      <span class="flap-mark"></span>
      <span class="flap-initials">LV</span>
    </div>
  </section>
</main>
</body>
</html>
```